Copper Lantern Gin

The gin is 100% proof and men and anbody 18 - 30 year old will be a target market - the bottle is very distinctive and lends itself to a square label.

The bottle is curved with a large front face that lends itself to a striking design. There should be enough space around the label to show the black gin in the bottle as this is a feature.

The current bottle with the existing label is attached below as is the new glass bottle. The new gin will be coloured black.

Font styles to use
Decorative
Script

```html
<!DOCTYPE html>
<html lang="en">
<head>
<meta charset="utf-8">
<title>Copper Lantern Gin – Label</title>
<link href="https://fonts.googleapis.com/css2?family=Kaushan+Script&family=Tinos:ital,wght@0,400;1,400&display=swap" rel="stylesheet">
<style>
  :root {
    --page-bg: #ffffff;
    --label-edge: #141416;
    --label-mid: #262628;
    --ink-silver: #c9c9cb;
    --ink-soft: #a9a9ab;
    --rule: #6d6d70;
    --art-red: #4a1414;
    --art-dark: #1e1516;
  }
  html, body {
    margin: 0;
    padding: 0;
    width: 968px;
    height: 1200px;
    overflow: hidden;
    background: var(--page-bg);
  }
  .canvas {
    position: relative;
    width: 968px;
    height: 1200px;
  }
  .label {
    position: absolute;
    left: 34px;
    top: 332px;
    width: 900px;
    height: 536px;
    background: linear-gradient(90deg, var(--label-edge) 0%, var(--label-mid) 30%, var(--label-mid) 70%, var(--label-edge) 100%);
    font-family: "Tinos", "Times New Roman", serif;
    color: var(--ink-silver);
  }
  .brand-name {
    position: absolute;
    left: 0;
    width: 100%;
    text-align: center;
    font-family: "Kaushan Script", cursive;
    font-weight: 400;
    font-size: 78px;
    line-height: 1.1;
    color: var(--ink-silver);
    margin: 0;
  }
  .brand-name--top { top: 44px; }
  .brand-name--bottom { top: 292px; }
  .emblem-art {
    position: absolute;
    left: 240px;
    top: 150px;
    width: 390px;
    height: 148px;
    border-radius: 6px;
    background: radial-gradient(ellipse at 60% 50%, var(--art-red) 0%, var(--art-dark) 60%, var(--label-mid) 100%);
  }
  .product-line {
    position: absolute;
    left: 0;
    top: 446px;
    width: 100%;
    text-align: center;
    font-style: italic;
    font-size: 26px;
    line-height: 1.2;
    color: var(--ink-soft);
    margin: 0;
  }
  .divider {
    position: absolute;
    left: 358px;
    top: 482px;
    width: 184px;
    height: 1px;
    background: var(--rule);
  }
  .volume-line {
    position: absolute;
    left: 0;
    top: 490px;
    width: 100%;
    text-align: center;
    font-size: 23px;
    line-height: 1.2;
    color: var(--ink-soft);
    margin: 0;
    word-spacing: 2px;
  }
  .volume-line .unit-size { font-style: italic; }
</style>
</head>
<body>
  <main class="canvas">
    <section class="label">
      <div class="emblem-art" role="img" aria-label="Decorative illustration of a prowling animal in tribal line style, silver on dark red"></div>
      <h1 class="brand-name brand-name--top">Copper</h1>
      <p class="brand-name brand-name--bottom">Lantern</p>
      <p class="product-line">Navy strength British Gyn</p>
      <div class="divider"></div>
      <p class="volume-line"><span class="unit-size">50</span> cl &nbsp; 57 % abv</p>
    </section>
  </main>
</body>
</html>
```